Stationery Design Project

Company name - Harborline Med

Wellness Consulting and training company. Run as a medical centre.
Logo design created already.
Looking for simplistic, yet innovative look.
Logo colours are blue and orange, so looking for something along those lines.

1) Need letter head with logo

2) Pen design

3) Cup - Drinking

4) Envelope

5) Business card - Launched as a separate project

No website yet.

Reason: Need business card and stationary design completed in these 5 days

Target Market(s)

35 to 60
Trendy and new age

Industry/Entity Type

Training

Colors
f37122
0255a3

Requirements
Must have
• Colours - Blue and orange
Nice to have
• Not too gaudy, but simple and succinct.

```html
<!DOCTYPE html>
<html lang="en">
<head>
<meta charset="utf-8">
<title>Harborline Med – Business Card</title>
<link href="https://fonts.googleapis.com/css2?family=Questrial&display=swap" rel="stylesheet">
<style>
  :root {
    --brand-blue: #0255a3;
    --brand-orange: #f37122;
    --navy: #0b3a6e;
    --navy-deep: #062a52;
    --ink: #4a4a4a;
    --ink-soft: #5c5c5c;
    --paper: #fbfbfa;
    --backdrop: #e6e8ec;
    --divider: #e4e4e2;
  }
  * { margin: 0; padding: 0; box-sizing: border-box; }
  html, body { width: 1200px; height: 800px; overflow: hidden; }
  body {
    background: var(--backdrop);
    font-family: "Questrial", "Century Gothic", sans-serif;
    display: flex;
    align-items: center;
    justify-content: center;
    gap: 60px;
  }
  .card {
    width: 510px;
    height: 320px;
    border-radius: 4px;
    position: relative;
    box-shadow: 0 6px 20px rgba(0,0,0,.12);
  }

  /* Front */
  .card-front { background: var(--paper); color: var(--ink); }
  .card-front .identity {
    position: absolute;
    left: 34px;
    top: 118px;
    width: 245px;
    text-align: right;
  }
  .brand-name {
    display: inline-flex;
    align-items: center;
    gap: 10px;
    font-size: 35px;
    line-height: 1;
    color: var(--brand-blue);
    letter-spacing: -0.5px;
    white-space: nowrap;
  }
  .brand-dot {
    width: 14px; height: 14px;
    border-radius: 50%;
    background: var(--brand-orange);
    flex: none;
  }
  .address {
    margin-top: 20px;
    font-size: 15px;
    line-height: 1.4;
    color: var(--ink-soft);
  }
  .divider {
    position: absolute;
    left: 300px;
    top: 40px;
    bottom: 40px;
    width: 1px;
    background: var(--divider);
  }
  .contact {
    position: absolute;
    left: 322px;
    top: 62px;
  }
  .person-name {
    font-size: 19px;
    font-weight: 400;
    letter-spacing: 0.5px;
    color: #3e3e3e;
  }
  .person-title {
    font-size: 14px;
    color: var(--ink-soft);
    margin-top: 4px;
  }
  .contact-list {
    list-style: none;
    margin-top: 22px;
    font-size: 13.5px;
    color: var(--ink-soft);
  }
  .contact-list li {
    display: flex;
    align-items: center;
    gap: 8px;
    height: 19px;
  }
  .contact-list svg { width: 14px; height: 14px; flex: none; }

  /* Back */
  .card-back {
    background: linear-gradient(135deg, var(--navy) 0%, var(--navy-deep) 100%);
    display: flex;
    align-items: center;
    justify-content: center;
  }
  .card-back .brand-name { color: #ffffff; font-size: 44px; }
  .card-back .brand-dot { width: 18px; height: 18px; }
</style>
</head>
<body>

<section class="card card-front" aria-label="Business card, front">
  <div class="identity">
    <div class="brand-name"><span class="brand-dot"></span>Harborline Med</div>
    <p class="address">Lindenweg 12, 60311<br>Frankfurt am Main</p>
  </div>

  <div class="divider"></div>

  <div class="contact">
    <h1 class="person-name">DR. ELIAS MARREN</h1>
    <p class="person-title">General Manager</p>
    <ul class="contact-list">
      <li>
        <svg viewBox="0 0 14 14" fill="none" stroke="var(--brand-blue)" stroke-width="1"><circle cx="7" cy="7" r="6.3"/><rect x="5" y="3.3" width="4" height="7.4" rx="0.7"/><line x1="6.4" y1="9.4" x2="7.6" y2="9.4"/></svg>
        +49 69 555 0142
      </li>
      <li>
        <svg viewBox="0 0 14 14" fill="none" stroke="var(--brand-blue)" stroke-width="1"><circle cx="7" cy="7" r="6.3"/><path d="M4.6 4c.6-.5 1.1-.4 1.4.1l.5 1c.2.4 0 .7-.3 1l-.3.3c.3.8.9 1.4 1.7 1.7l.3-.3c.3-.3.6-.5 1-.3l1 .5c.5.3.6.8.1 1.4-.6.7-1.5.8-2.4.4-1.5-.7-2.6-1.8-3.3-3.3-.4-.9-.3-1.8.3-2.5z" fill="var(--brand-blue)" stroke="none"/></svg>
        +49 69 555 0187
      </li>
      <li>
        <svg viewBox="0 0 14 14" fill="none" stroke="var(--brand-blue)" stroke-width="1"><circle cx="7" cy="7" r="6.3"/><rect x="3.8" y="4.8" width="6.4" height="4.4" fill="var(--brand-blue)" stroke="none"/><path d="M3.8 4.8 7 7.3l3.2-2.5" stroke="#fff" stroke-width="0.8"/></svg>
        info@harborlinemed.com
      </li>
      <li>
        <svg viewBox="0 0 14 14" fill="none" stroke="var(--brand-blue)" stroke-width="1"><circle cx="7" cy="7" r="6.3"/><ellipse cx="7" cy="7" rx="2.6" ry="6.3"/><line x1="0.7" y1="7" x2="13.3" y2="7"/><path d="M1.8 4h10.4M1.8 10h10.4"/></svg>
        www.harborlinemed.com
      </li>
    </ul>
  </div>
</section>

<section class="card card-back" aria-label="Business card, back">
  <div class="brand-name"><span class="brand-dot"></span>Harborline Med</div>
</section>

</body>
</html>
```